Dastrelo's New Trucking Company Website

We are wanting to create a basic website for “Dastrelo Trucking” on www.DastreloTrucking.example.

The first attachment titled “write-up” has 7 sections listed, which we would like as tabs at the top of the website, followed by the write up of that section. (The sections ‘employment’ and ‘requirements’ should be under one section).

We would like the landing page to be that of a photo of a Dastrelo Truck. Please see attachment two “Dastrelo_truck” as an example of what our truck looks like. We would like this to be of better quality/more pleasing to the eye. The rest of the attachments (attachment 3- attachment 7) are of possible photos/ideas.

Woould you be able to photoshop any of those trucks to look like our Dastrelo Truck on to a pretty highway/background etc?

We would like this main photo be a constant background of the website, even when you click around the website and the language changes.

Target Market(s)

Northwest Based Companies seeking Transportation needs, grocery stores, Truck Drivers

Industry/Entity Type

Trucking Company

Number of Pages Required

5+ page

Font styles to use
Sans Serif

Requirements
Must have
• Must have one really good photo of our truck (or a truck that looks like ours) as the main photo on the page. This photo must stay consistent as the background when people click on the tabs/sections below.
Nice to have
• Clean/simple layout
Should not have
• Dull colors/ disorganized.

```html
<!DOCTYPE html>
<html lang="en">
<head>
<meta charset="utf-8">
<title>Dastrelo Trucking</title>
<link rel="stylesheet" href="https://fonts.googleapis.com/css2?family=Open+Sans:ital,wght@0,400;0,600;0,700;0,800;1,400&family=Montserrat:wght@600;700&display=swap">
<style>
:root{
  --teal:#45b5d1;
  --teal-dark:#3aa2bd;
  --navy:#2c3a4a;
  --nav:#35424f;
  --ink:#333a42;
  --muted:#8a9096;
  --pale:#b3b9be;
  --line:#e4e7ea;
  --field:#eef0f2;
  --green:#7cc242;
  --footer:#2a333e;
}
*{box-sizing:border-box;margin:0;padding:0}
html,body{width:1200px;height:3543px;overflow:hidden}
body{position:relative;background:#fff;font-family:"Open Sans",Arial,sans-serif;color:var(--ink)}
section,header,nav,footer,.topbar{position:absolute;left:0;width:1200px}
.abs{position:absolute}

/* top bar */
.topbar{top:0;height:47px;background:#f3f4f5;border-bottom:1px solid var(--line)}
.topbar .mail{left:71px;top:14px;font-size:14px;color:#555;display:flex;align-items:center;gap:10px}
.topbar .social{right:230px;top:0;display:flex}
.topbar .social span{width:46px;height:47px;border-left:1px solid var(--line)}
.topbar .quote{right:0;top:0;width:230px;height:47px;background:var(--teal);color:#fff;font-size:13px;font-weight:700;letter-spacing:.5px;display:flex;align-items:center;justify-content:center}

/* header */
header{top:47px;height:76px;background:#fff}
.brand{left:71px;top:18px;font-size:34px;font-weight:600;color:var(--teal);letter-spacing:-.5px}
.callus{right:71px;top:18px;display:flex;align-items:center;gap:12px}
.callus small{font-size:10px;line-height:12px;font-weight:700;color:var(--ink);text-transform:uppercase}
.callus strong{font-size:31px;font-weight:600;color:var(--ink)}

/* nav */
nav{top:123px;height:35px;background:var(--nav)}
nav ul{list-style:none;display:flex;position:absolute;left:71px;top:0}
nav li{color:#fff;font-size:12px;font-weight:700;text-transform:uppercase;line-height:35px;margin-right:44px}
nav .search{right:71px;top:8px}

/* hero */
.hero{top:158px;height:456px;background:linear-gradient(180deg,#6b7a4e 0%,#8b5e3a 38%,#a86b3c 55%,#6f7070 78%,#8f9294 100%)}
.hero .mission{left:80px;top:250px;font-size:30px;line-height:44px;font-weight:600;color:#fff;text-shadow:0 1px 3px rgba(0,0,0,.4)}
.hero .dot{top:212px;width:26px;height:26px;border-radius:50%;background:rgba(255,255,255,.45)}

/* intro */
.intro{top:614px;height:284px;background:#fff}
.intro h2{left:71px;top:24px;font-size:29px;line-height:35px;font-weight:800;color:var(--ink);text-transform:uppercase}
.btn{background:var(--teal);color:#fff;font-size:13px;display:flex;align-items:center;justify-content:center}
.intro .btn{left:992px;top:36px;width:137px;height:33px}
.intro p{left:71px;top:146px;width:1058px;font-size:14px;line-height:27px;color:var(--pale)}

/* services */
.services{top:898px;height:420px;background:linear-gradient(180deg,#eceded 0%,#e3e3e1 60%,#d8d6cf 100%)}
.services h2{left:0;width:1200px;top:36px;text-align:center;font-size:34px;font-weight:700;color:var(--ink)}
.services .sub{left:0;width:1200px;top:96px;text-align:center;font-size:15px;color:var(--muted)}
.card{top:155px;width:335px;height:201px;background:#fff;padding:26px 18px}
.card h3{font-size:16px;font-weight:600;color:var(--ink);margin:10px 0 10px}
.card p{font-size:11px;line-height:17px;color:#777}
.services .arrow{top:236px;width:26px;height:26px;border-radius:50%;background:#fff;display:flex;align-items:center;justify-content:center}

/* employment */
.employment{top:1318px;height:709px;background:#fff}
.employment h2{top:38px;font-size:35px;font-weight:700;color:var(--ink)}
.employment .lead{left:71px;top:122px;width:450px;font-size:17px;line-height:26px;color:#666}
.employment .pay{left:71px;top:214px;width:500px;font-size:22px;line-height:32px;color:#555}
.employment .pay b{color:var(--teal);font-weight:700}
.perks{left:71px;top:348px;list-style:none}
.perks li{font-size:32px;line-height:59px;color:#444}
.perks li::before{content:"\2022";margin-right:12px}
.employment .note{left:71px;top:550px;width:480px;font-size:17px;line-height:24px;color:#888;font-style:italic}
.employment .note b{color:#333;font-weight:700}
.reqs{left:640px;top:120px;width:480px;list-style:none}
.reqs li{font-size:18px;line-height:39px;color:var(--pale)}
.reqs li::before{content:"\2022";color:var(--teal);margin-right:6px}

/* calculator */
.calc{top:2027px;height:531px;background:linear-gradient(90deg,#3d4044 0%,#5f6266 45%,#46494d 100%)}
.calc .kicker{left:94px;width:492px;top:58px;text-align:center;font-size:11px;letter-spacing:1px;color:#b8bcc0;text-transform:uppercase}
.calc h2{left:94px;width:492px;top:76px;text-align:center;font-family:"Montserrat",sans-serif;font-size:34px;font-weight:700;color:#fff}
.field{height:36px;background:#fff;font-size:13px;color:#777;padding:0 14px;display:flex;align-items:center;justify-content:space-between}
.calc .label{font-size:12px;color:#fff}
.toggle{width:56px;height:22px;border-radius:11px;background:#fff;border:2px solid #fff}
.total{left:444px;top:427px;width:142px;height:36px;background:var(--green);color:#fff;font-size:13px;padding-left:14px;display:flex;align-items:center}
.info{width:232px;height:204px;background:rgba(232,240,247,.93);padding:22px 24px}
.info h3{font-family:"Montserrat",sans-serif;font-size:18px;font-weight:600;color:var(--ink);margin-bottom:10px}
.info p{font-size:13px;line-height:19px;color:#666;margin-bottom:14px}
.info .btn{width:100px;height:28px;font-size:12px;position:static}

/* contact */
.contact{top:2558px;height:584px;background:#fff}
.contact h2{left:0;width:1200px;top:38px;text-align:center;font-size:36px;font-weight:700;color:var(--ink)}
.cline{left:71px;display:flex;align-items:center;gap:22px;font-size:17px;color:#555}
.map{left:71px;top:305px;width:371px;height:220px;background:linear-gradient(135deg,#e9e4d6,#d9e3cf 50%,#cfdbe4)}
.input{height:36px;background:var(--field);font-size:12px;color:#888;padding:0 14px;display:flex;align-items:center}
.submit{left:501px;top:484px;width:125px;height:38px;background:var(--teal);color:#fff;font-size:13px;font-weight:700;letter-spacing:1px;display:flex;align-items:center;justify-content:center}

/* footer */
footer{top:3142px;height:401px;background:var(--footer);color:#c6ccd2}
footer h4{top:58px;font-size:13px;font-weight:700;color:#fff;text-transform:uppercase}
.qlinks{font-size:11px;color:#c6ccd2;text-transform:uppercase}
.qlinks div{height:38px;border-bottom:1px solid #3b4550;display:flex;align-items:center}
footer .small{font-size:11px;line-height:20px;color:#c6ccd2}
footer .small b{color:#fff}
.newsletter{left:775px;top:206px;width:280px;height:40px;background:#3c4753;font-size:11px;color:#8d96a0;padding-left:14px;display:flex;align-items:center}
.send{left:1055px;top:206px;width:40px;height:40px;background:var(--teal);display:flex;align-items:center;justify-content:center}
.bottom{top:336px;left:80px;width:1040px;font-size:11px;color:#aab2ba;display:flex;justify-content:space-between}
.bottom b{color:#fff;font-weight:600}
.bottom nav{position:static;background:none;height:auto;width:auto;display:flex;gap:28px}
</style>
</head>
<body>

<div class="topbar">
  <div class="abs mail">
    <svg width="16" height="12" viewBox="0 0 16 12"><rect x="0.5" y="0.5" width="15" height="11" fill="#555"/><path d="M1 1l7 6 7-6" fill="none" stroke="#fff" stroke-width="1.4"/></svg>
    Email us at : hello@dastrelo.example
  </div>
  <div class="abs social"><span></span><span></span><span></span></div>
  <div class="abs quote">REQUEST A QUOTE</div>
</div>

<header>
  <div class="abs brand">Dastrelo Trucking</div>
  <div class="abs callus">
    <svg width="22" height="34" viewBox="0 0 22 34"><rect x="2" y="1" width="18" height="32" rx="3" fill="none" stroke="#333a42" stroke-width="2.5"/><circle cx="11" cy="28" r="1.8" fill="#333a42"/></svg>
    <small>Call us now for<br>your transport</small>
    <strong>555 0190 123</strong>
  </div>
</header>

<nav>
  <ul><li>Home</li><li>About us</li><li>Services</li><li>What we do</li><li>Shipping calculator</li><li>Contact</li></ul>
  <svg class="abs search" width="18" height="18" viewBox="0 0 18 18"><circle cx="7.5" cy="7.5" r="5.5" fill="none" stroke="#45b5d1" stroke-width="2.2"/><path d="M11.5 11.5l5 5" stroke="#45b5d1" stroke-width="2.4"/></svg>
</nav>

<section class="hero" role="img" aria-label="Red semi truck with white trailer driving along a curving highway through autumn forest">
  <div class="abs dot" style="left:30px"></div>
  <div class="abs dot" style="right:30px"></div>
  <p class="abs mission">Our mission is to provide the best customer<br>service and trucking services in the Northwest</p>
</section>

<section class="intro">
  <h2 class="abs">We offer quick &amp; powerful solution<br>for transport services</h2>
  <div class="abs btn">Read More</div>
  <p class="abs">Dastrelo Trucking LLC was created in 2012 to assist its parent company, Dastrelo Gourmet, in transporting product from our Seattle HQ to our Portland distribution center every night. Approximately four years later, Dastrelo Trucking has expanded to meet the growing needs of our sister company as well as many Northwest based companies looking to transport chilled, frozen and dry product. We now operate a fleet of semis and large box trucks for local and regional distribution throughout the Pacific Northwest.</p>
</section>

<section class="services">
  <h2 class="abs">OUR SERVICES</h2>
  <p class="abs sub">Our mission is to provide the best customer service and trucking services in the Northwest.</p>
  <div class="abs arrow" style="left:20px"><svg width="8" height="10" viewBox="0 0 8 10"><path d="M6 1L2 5l4 4" fill="none" stroke="#666" stroke-width="1.6"/></svg></div>
  <div class="abs arrow" style="right:20px"><svg width="8" height="10" viewBox="0 0 8 10"><path d="M2 1l4 4-4 4" fill="none" stroke="#666" stroke-width="1.6"/></svg></div>
  <div class="abs card" style="left:71px">
    <svg width="36" height="26" viewBox="0 0 36 26"><rect x="1" y="3" width="20" height="15" fill="#45b5d1"/><path d="M22 8h7l5 6v4H22z" fill="#45b5d1"/><circle cx="8" cy="21" r="3.5" fill="#fff" stroke="#45b5d1" stroke-width="2"/><circle cx="28" cy="21" r="3.5" fill="#fff" stroke="#45b5d1" stroke-width="2"/></svg>
    <h3>Dispatch</h3>
    <p>Dastrelo Trucking offers refrigerated services in and around Seattle and the Pacific Northwest. We're equipped with 100% real time GPS and our drivers are electronically dispatched.</p>
  </div>
  <div class="abs card" style="left:435px">
    <svg width="28" height="28" viewBox="0 0 28 28"><path d="M4 24L20 8M8 4l16 16" stroke="#333a42" stroke-width="3.5" stroke-linecap="round"/><circle cx="21" cy="7" r="4" fill="none" stroke="#333a42" stroke-width="2.5"/></svg>
    <h3>Equipment</h3>
    <p>Dastrelo Trucking provides a variety of transportation, warehousing, crossdocking, transportation, loading, and distribution services. We have heavy haul 53' trailers, which are both refrigerated and non-refrigerated.</p>
  </div>
  <div class="abs card" style="left:794px">
    <svg width="30" height="28" viewBox="0 0 30 28"><path d="M2 13a13 11 0 0 1 26 0z" fill="#45b5d1"/><path d="M15 13v10a3 3 0 0 1-6 0" fill="none" stroke="#45b5d1" stroke-width="2.2"/></svg>
    <h3>Insurance</h3>
    <p>Dastrelo Trucking is fully insured against the risks associated with today's trucking environment and we are in good standing. A copy of our insurance certificate is available upon request. Please contact your Dastrelo Trucking representative for assistance.</p>
  </div>
</section>

<section class="employment">
  <h2 class="abs" style="left:71px">Employment</h2>
  <h2 class="abs" style="left:640px">Minimum Requirements</h2>
  <p class="abs lead">We are currently accepting Driver Applications for immediate employment in Washington State.</p>
  <p class="abs pay">Dastrelo Trucking drivers receive a <b>starting pay of $19.00/hour + DOE.</b> Additional benefits employees receive are:</p>
  <ul class="abs perks"><li>Medical, Dental, 401k, Vacation</li><li>Harwick Fleet</li><li>Paid Holidays</li></ul>
  <p class="abs note">Having a Hazmat endorsement, Port of Seattle/Port of Tacoma terminal experience, and/or having heavy-haul experience is a plus. Please email all resumes to <b>Marisol@dastrelogourmet.example.</b></p>
  <ul class="abs reqs">
    <li>Minimum age of 24 years old</li>
    <li>Class “A” (CDL)</li>
    <li>TWIC card (TWIC) or willing/able to obtain<br>one</li>
    <li>Two years of verifiable experience in a<br>tractor-trailer</li>
    <li>No more than three (3) moving violations<br>in prior three-year-period</li>
    <li>No serious traffic violations (DOT defined)<br>in the prior three-year-period</li>
    <li>No more than one (1) at-fault accident in<br>prior three-year-period</li>
    <li>No positive alcohol or drug tests in the<br>prior two-year-period</li>
  </ul>
</section>

<section class="calc" role="img" aria-label="Dark toned background photo of a logistics worker with cargo">
  <p class="abs kicker">Check the costs</p>
  <h2 class="abs">Shipping Calculator</h2>
  <div class="abs field" style="left:94px;top:144px;width:492px">Truckload type <span>&#9662;</span></div>
  <div class="abs field" style="left:94px;top:195px;width:237px">Height (cm)</div>
  <div class="abs field" style="left:350px;top:195px;width:236px">Width (cm)</div>
  <div class="abs field" style="left:94px;top:252px;width:237px">Depth (cm)</div>
  <div class="abs field" style="left:350px;top:252px;width:236px">Weight (kg)</div>
  <span class="abs label" style="left:94px;top:318px">Distance (km)</span>
  <span class="abs label" style="left:560px;top:318px">0 km</span>
  <div class="abs" style="left:94px;top:345px;width:492px;height:4px;background:#fff"></div>
  <div class="abs" style="left:94px;top:338px;width:16px;height:16px;border-radius:50%;background:var(--green)"></div>
  <div class="abs field" style="left:94px;top:373px;width:492px">Type of service <span>&#9662;</span></div>
  <span class="abs label" style="left:94px;top:437px">Add insurance</span>
  <div class="abs toggle" style="left:190px;top:434px"><div style="width:18px;height:18px;border-radius:50%;background:#444"></div></div>
  <div class="abs total">Total: $ 0</div>

  <div class="abs info" style="left:614px;top:56px"><h3>Get a Free Quote!</h3><p>Nulla venenatis. In pede mi, aliquet sit amet, euismod in, auctor ut, ligula.</p><div class="btn">Start a Quote</div></div>
  <div class="abs info" style="left:874px;top:56px"><h3>Shipment Tracking</h3><p>Aliquam dapibus tincidunt metus. Praesent justo dolor, lobortis quis, lobortis dignissim.</p><div class="btn">Find Your Cargo</div></div>
  <div class="abs info" style="left:614px;top:288px"><h3>Our Locations</h3><p>Sed laoreet leo. Ut tellus dolor, dapibus eget, elementum vel, cursus eleifend, elit.</p><div class="btn">Get Estimate</div></div>
  <div class="abs info" style="left:874px;top:288px"><h3>Have a Question?</h3><p>Donec sagittis euismod purus. Sed ut perspiciatis unde omnis iste natus error.</p><div class="btn">Contact Us</div></div>
</section>

<section class="contact">
  <h2 class="abs">Contact us</h2>
  <div class="abs cline" style="top:122px">
    <svg width="26" height="22" viewBox="0 0 26 22"><path d="M13 1L1 11h3v10h7v-6h4v6h7V11h3z" fill="#45b5d1"/></svg>
    27 Harlow Lane, Brinmouth, England
  </div>
  <div class="abs cline" style="top:186px">
    <svg width="26" height="22" viewBox="0 0 26 22"><path d="M5 1l5 5-3 3c2 4 5 7 9 9l3-3 5 5-3 3C11 22 2 12 2 4z" fill="#45b5d1"/></svg>
    +1 (555) 014 226
  </div>
  <div class="abs cline" style="top:246px">
    <svg width="26" height="20" viewBox="0 0 26 20"><rect x="1" y="1" width="24" height="18" fill="none" stroke="#45b5d1" stroke-width="2"/><path d="M1 1l12 10 12-10" fill="none" stroke="#45b5d1" stroke-width="2"/></svg>
    support@northline.example
  </div>
  <div class="abs map" role="img" aria-label="Street map showing the office location"></div>
  <div class="abs input" style="left:501px;top:182px;width:286px">First name..</div>
  <div class="abs input" style="left:810px;top:182px;width:291px">Last name..</div>
  <div class="abs input" style="left:501px;top:241px;width:286px">Email address..</div>
  <div class="abs input" style="left:810px;top:241px;width:291px">Phone..</div>
  <div class="abs input" style="left:501px;top:300px;width:600px;height:161px;align-items:flex-start;padding-top:12px">Write..</div>
  <div class="abs submit">SUBMIT</div>
</section>

<footer>
  <h4 class="abs" style="left:80px">Quick links</h4>
  <h4 class="abs" style="left:428px">Contact us</h4>
  <h4 class="abs" style="left:775px">Newsletter signup</h4>
  <div class="abs qlinks" style="left:80px;top:114px;width:148px"><div>Home</div><div>About us</div><div>Services</div><div>What we do</div></div>
  <div class="abs qlinks" style="left:240px;top:114px;width:148px"><div>Shipping calculator</div><div>Contact</div></div>
  <div class="abs small" style="left:428px;top:128px;width:300px">
    <b>TRANSPORT</b><br>Contact Address will appear here, some text gonna appear here, New York City, - 10001, USA<br><br>
    <b>Phone :</b> 555 0190 123<br><b>Email :</b> office@dastrelo.example
  </div>
  <p class="abs small" style="left:775px;top:128px;width:320px">If you want receive our all weekly updates about new offers and discount, signup below.</p>
  <div class="abs newsletter">Email Address</div>
  <div class="abs send"><svg width="18" height="16" viewBox="0 0 18 16"><path d="M1 8l16-7-4 14-4-5z" fill="#fff"/></svg></div>
  <div class="abs bottom">
    <span>Copyright 2017. All Rights Reserved by <b>Dastrelo Trucking</b></span>
    <nav><span>Terms Of Use</span><span>Legal Desclaimer</span><span>Privacy Policy</span><span>Support</span><span>Sitemap</span></nav>
  </div>
</footer>

</body>
</html>
```